New cool to-go cup for KELMO Coffee

UPDATE MARCH 18: Please read the attached document "Design ideas - Front" with a mock-up of the design we are looking for. And please don't change the logo.

We are looking for a new cool design for our to-go cups in kraft paper (same style as the attached photo).

The idea:

We have three different cups sizes: 6oz, 8oz and 12oz. We call them “Tiny-Lark” (6oz), “Mid-Wren” (8oz) and “Tall-heron” (12oz) (refers to the size in milliliters). We would like to include this in the cup design. Please see the attached sketch of the idea ("Design ideas - Front").

The backside of the cup should have the attached text and logo ("Design ideas - Back").

But other ideas are also very welcome too! Maybe just a simple cup with the logo.

Please keep the design very minimalistic. The more simple the better.

Target Market(s)

Young urban people

Industry/Entity Type

Coffee shop

Font styles to use
Sans Serif

Requirements
Must have
• Kraft paper cups

```html
<!DOCTYPE html>
<html lang="en">
<head>
<meta charset="utf-8">
<title>KELMO Coffee – To-go Cup Wrap</title>
<link rel="stylesheet" href="https://fonts.googleapis.com/css2?family=Alegreya+Sans:wght@400;700&family=Neucha&family=Special+Elite&family=Playfair+Display+SC:wght@700&family=Parisienne&family=Lustria&family=Lobster&family=Pompiere&family=Raleway:wght@400&family=Great+Vibes&family=Kaushan+Script&family=Oswald:wght@300&family=Poiret+One&family=Cormorant+Garamond:wght@500&family=Abril+Fatface&family=Anton&display=swap">
<style>
  :root {
    --paper: #ffffff;
    --ink: #141414;
    --brand: #3b2418;
    --frame: #a6a6a6;
  }
  * { margin: 0; padding: 0; box-sizing: border-box; }
  html, body { width: 976px; height: 1200px; overflow: hidden; background: var(--paper); }
  .sheet {
    position: relative;
    width: 976px;
    height: 1200px;
    background: var(--paper);
    font-family: "Alegreya Sans", sans-serif;
    color: var(--ink);
  }
  .wrap-front {
    position: absolute;
    left: 44px;
    top: 130px;
    width: 888px;
    height: 385px;
    border: 1px solid var(--frame);
  }
  .wrap-front svg { display: block; width: 100%; height: 100%; }
  .tag { fill: var(--ink); }
  .brand-ring { fill: none; stroke: var(--brand); stroke-width: 5; }
  .brand-name {
    fill: var(--brand);
    font-family: "Alegreya Sans", sans-serif;
    font-weight: 700;
    font-size: 34px;
    letter-spacing: 3px;
  }
  .back-panel {
    position: absolute;
    left: 0;
    top: 620px;
    width: 976px;
    display: flex;
    flex-direction: column;
    align-items: center;
  }
  .back-badge {
    width: 200px;
    height: 200px;
    border: 6px solid var(--brand);
    border-radius: 50%;
    display: flex;
    align-items: center;
    justify-content: center;
    color: var(--brand);
    font-weight: 700;
    font-size: 40px;
    letter-spacing: 4px;
  }
  .back-copy {
    margin-top: 34px;
    text-align: center;
    font-size: 30px;
    line-height: 1.3;
  }
  .back-copy .contact { font-weight: 700; }
</style>
</head>
<body>
<main class="sheet">
  <section class="wrap-front" aria-label="Cup wrap, front">
    <svg viewBox="0 0 986 427" xmlns="http://www.w3.org/2000/svg">
      <text class="tag" x="88" y="72" font-family="Neucha, sans-serif" font-size="40">#tinylark</text>
      <text class="tag" x="378" y="77" font-family="'Special Elite', monospace" font-size="40" transform="rotate(5 378 77)">#tinylark</text>
      <text class="tag" x="698" y="95" font-family="'Playfair Display SC', serif" font-weight="700" font-size="34">#tinylark</text>
      <text class="tag" x="25" y="150" font-family="Parisienne, cursive" font-size="32" transform="rotate(3 25 150)">#tinylark</text>
      <text class="tag" x="185" y="205" font-family="Lustria, serif" font-size="46" transform="rotate(-20 185 205)">#tinylark</text>
      <text class="tag" x="265" y="220" font-family="Lobster, cursive" font-size="32" transform="rotate(3 265 220)">#tinylark</text>
      <text class="tag" x="633" y="200" font-family="Pompiere, sans-serif" font-size="66" transform="rotate(-8 633 200)">#TINYLARK</text>
      <text class="tag" x="733" y="250" font-family="Raleway, sans-serif" font-size="40">#tinylark</text>
      <text class="tag" x="25" y="282" font-family="'Great Vibes', cursive" font-size="44">#tinylark</text>
      <text class="tag" x="241" y="282" font-family="'Kaushan Script', cursive" font-size="34">#tinylark</text>
      <text class="tag" x="303" y="350" font-family="Oswald, sans-serif" font-weight="300" font-size="44">#tinylark</text>
      <text class="tag" x="123" y="390" font-family="'Poiret One', sans-serif" font-size="44">#TINYLARK</text>
      <text class="tag" x="485" y="392" font-family="'Cormorant Garamond', serif" font-weight="500" font-size="44">#TINYLARK</text>
      <text class="tag" x="596" y="305" font-family="'Abril Fatface', serif" font-size="44" transform="rotate(5 596 305)">#tinylark</text>
      <text class="tag" x="796" y="385" font-family="Anton, sans-serif" font-size="34" transform="rotate(-20 796 385)">#tinylark</text>
      <g class="brand-mark">
        <circle class="brand-ring" cx="503" cy="214" r="88"/>
        <text class="brand-name" x="503" y="226" text-anchor="middle">KELMO</text>
      </g>
    </svg>
  </section>

  <section class="back-panel" aria-label="Cup wrap, back">
    <div class="back-badge">KELMO</div>
    <p class="back-copy">
      Read about your coffee and<br>
      the dedicated farmers<br>
      who made this cup possible:<br>
      <span class="contact">www.kelmo-cups.com</span><br>
      <span class="contact">@kelmocups</span>
    </p>
  </section>
</main>
</body>
</html>
```